Velmar Industrial Coatings

We are looking to improve our business cards. Our company installs industrial floor and wall coatings in industrial, chemical and food processing plants.
Our coatings which consist of epoxy, urethane, and vinyl esters provide chemical and abrasion resistant surface with non-skid properties that are easy to clean.

Target Market(s)

food manufacturing, chemical plants, breweries and wineries, warehouses, clean room floors.

Industry/Entity Type

Construction

Contact Information for Business Card

improved current logo.

Colors

Designer to choose colors to be used in the design.

Requirements
Must have
• the information from uploaded file
Nice to have
• "We'll be outstanding on your floors."

```html
<!DOCTYPE html>
<html lang="en">
<head>
<meta charset="utf-8">
<title>Velmar Industrial Coatings – Business Card</title>
<link rel="stylesheet" href="https://fonts.googleapis.com/css2?family=Roboto:wght@400;500&display=swap">
<style>
  :root {
    --bg: #c9c9c9;
    --navy: #232f7d;
    --navy-line: #2c3988;
    --white: #ffffff;
    --paper-fade: #ececec;
    --grey-text: #6f6f6f;
    --grey-rule: #9a9a9a;
  }
  * { box-sizing: border-box; margin: 0; padding: 0; }
  html, body { width: 1200px; height: 900px; overflow: hidden; }
  body {
    background: var(--bg);
    font-family: "Roboto", Arial, sans-serif;
    position: relative;
  }
  .card {
    position: absolute;
    left: 270px;
    width: 660px;
    height: 377px;
    box-shadow: 0 6px 18px rgba(0,0,0,0.25);
    overflow: hidden;
  }
  .card--front { top: 48px; background: var(--navy); }
  .card--back {
    top: 475px;
    background: linear-gradient(135deg, var(--paper-fade) 0%, var(--white) 55%);
  }

  /* front */
  .front-texture {
    position: absolute; inset: 0;
    background: linear-gradient(160deg, var(--navy-line) 0%, var(--navy) 60%);
  }
  .front-brand {
    position: absolute;
    left: 0; right: 0; top: 50%;
    transform: translateY(-50%);
    display: flex; align-items: center; justify-content: center; gap: 18px;
  }
  .brand-square {
    width: 54px; height: 54px;
    background: var(--white);
    flex: none;
  }
  .front-brand .brand-name {
    color: var(--white);
    font-size: 30px;
    font-weight: 500;
    letter-spacing: 1px;
    text-transform: uppercase;
    line-height: 1.15;
    max-width: 330px;
  }

  /* back */
  .side-band {
    position: absolute; left: 0; top: 0; bottom: 0;
    width: 14px;
    background: var(--navy);
  }
  .back-brand {
    position: absolute; left: 56px; top: 70px;
    display: flex; align-items: center; gap: 14px;
  }
  .back-brand .brand-square { width: 42px; height: 42px; background: var(--navy); }
  .back-brand .brand-name {
    color: var(--navy);
    font-size: 22px;
    font-weight: 500;
    text-transform: uppercase;
    letter-spacing: 0.5px;
    line-height: 1.15;
    max-width: 230px;
  }
  .person {
    position: absolute; left: 422px; top: 58px;
  }
  .person-name {
    color: var(--navy);
    font-size: 19px;
    font-weight: 500;
    text-transform: uppercase;
  }
  .person-title {
    color: var(--grey-text);
    font-size: 15px;
    text-transform: uppercase;
    margin-top: 2px;
  }
  .divider {
    width: 44px; height: 2px;
    background: var(--grey-rule);
    margin: 20px 0 0 24px;
  }
  .contact-list {
    position: absolute; left: 400px; top: 162px;
    list-style: none;
  }
  .contact-list li {
    display: flex; align-items: center; gap: 8px;
    font-size: 15px;
    color: var(--grey-text);
    height: 21px;
  }
  .contact-list svg { width: 14px; height: 14px; flex: none; }
  .address {
    position: absolute; left: 56px; top: 262px;
    font-size: 16px; line-height: 1.3;
    color: var(--grey-text);
  }
  .address .address-company { color: var(--navy); }
</style>
</head>
<body>

<section class="card card--front">
  <div class="front-texture" role="img" aria-label="Navy background with a faint diamond lattice pattern"></div>
  <div class="front-brand">
    <span class="brand-square"></span>
    <span class="brand-name">Velmar Industrial Coatings Inc.</span>
  </div>
</section>

<section class="card card--back">
  <div class="side-band"></div>

  <div class="back-brand">
    <span class="brand-square"></span>
    <span class="brand-name">Velmar Industrial Coatings Inc.</span>
  </div>

  <div class="person">
    <div class="person-name">Reid Calloway</div>
    <div class="person-title">Founder</div>
    <div class="divider"></div>
  </div>

  <ul class="contact-list">
    <li>
      <svg viewBox="0 0 16 16" fill="var(--navy)"><path d="M4 1l3 3-2 2c1 2 3 4 5 5l2-2 3 3-2 2C7 14 2 9 2 3z"/></svg>
      (360) 555-0142
    </li>
    <li>
      <svg viewBox="0 0 16 16" fill="none" stroke="var(--navy)" stroke-width="1.6"><rect x="4" y="1" width="8" height="14" rx="1.5"/><line x1="7" y1="12.5" x2="9" y2="12.5"/></svg>
      (360) 555-0178
    </li>
    <li>
      <svg viewBox="0 0 16 16" fill="var(--navy)"><path d="M4 1l3 3-2 2c1 2 3 4 5 5l2-2 3 3-2 2C7 14 2 9 2 3z"/></svg>
      1-800-555-0196
    </li>
    <li>
      <svg viewBox="0 0 16 16" fill="var(--navy)"><rect x="4" y="1" width="8" height="5"/><rect x="1" y="6" width="14" height="7" rx="1"/><rect x="4" y="11" width="8" height="4" fill="var(--white)" stroke="var(--navy)"/></svg>
      (360) 555-0143
    </li>
    <li>
      <svg viewBox="0 0 16 16" fill="none" stroke="var(--navy)" stroke-width="1.6"><rect x="1" y="3" width="14" height="10"/><path d="M1 3l7 6 7-6"/></svg>
      reid@velmarfloors.com
    </li>
    <li>
      <svg viewBox="0 0 16 16" fill="none" stroke="var(--navy)" stroke-width="1.4"><circle cx="8" cy="8" r="6.5"/><ellipse cx="8" cy="8" rx="3" ry="6.5"/><line x1="1.5" y1="8" x2="14.5" y2="8"/></svg>
      www.velmarfloors.com
    </li>
  </ul>

  <address class="address" style="font-style: normal;">
    <div class="address-company">Velmar Inc.</div>
    <div>PO Box 214</div>
    <div>Alder Creek, WA 98000</div>
  </address>
</section>

</body>
</html>
```